My website design

It Will be a to-go website for all service requests from the comfort of your home. services ranging from renting an electrician to fix your home electrical issues, DJ for your party, mark-up artist for your wedding and so on. Here are a few websites for inspiration:

https://www.dwellpanel.example/
https://www.chorewren.example/
https://www.gigplover.example/

Number of Pages Required

5+ page

Requirements
Must have
• User's registration form
pros resgistation form
filling out job request form
quotes sent sent back to job requester from various pros within the same zip code
quote accepted
ability to review pros once jobs are completed

```html
<!DOCTYPE html>
<html lang="en">
<head>
<meta charset="utf-8">
<title>Fixora – Home Maintenance Made Simple</title>
<link rel="stylesheet" href="https://fonts.googleapis.com/css2?family=Poppins:wght@300;400;500;600;700&display=swap">
<style>
:root{
  --green:#35b24a;
  --green-soft:#eaf6ec;
  --ink:#1f2430;
  --slate:#4f5a66;
  --muted:#7b828c;
  --line:#dfe3e7;
  --grey-bg:#f5f6f7;
  --navy:#1c2238;
  --white:#ffffff;
}
*{box-sizing:border-box;margin:0;padding:0}
html,body{width:1200px;height:2752px;overflow:hidden}
body{font-family:"Poppins",sans-serif;color:var(--ink);background:var(--white);position:relative}
.abs{position:absolute}
.btn{display:inline-flex;align-items:center;justify-content:center;border-radius:4px;font-weight:500;font-size:15px;color:var(--white)}
.btn-green{background:var(--green)}
.btn-dark{background:var(--slate)}

/* nav */
.nav{top:0;left:0;width:1200px;height:80px;background:var(--white);z-index:3}
.brand{display:flex;align-items:center;gap:12px;font-weight:700;font-size:28px;letter-spacing:2px;color:var(--ink)}
.brand-dot{width:22px;height:22px;background:var(--green)}
.nav .brand{left:120px;top:20px}
.nav-links{left:500px;top:26px;display:flex;gap:48px;font-size:15px;font-weight:500}
.nav-links a{color:var(--ink);text-decoration:none}
.nav-links .active{color:var(--green);border-bottom:2px solid var(--green);padding-bottom:6px}
.nav .btn{left:920px;top:20px;width:186px;height:44px}

/* hero */
.hero{top:80px;left:0;width:1200px;height:560px;background:linear-gradient(90deg,#b9a58c 0%,#cbbfae 35%,#e8e4df 55%,#f4f4f4 70%,#f6f6f6 100%)}
.hero-photo{top:0;left:0;width:700px;height:560px;background:linear-gradient(160deg,#d5cbbd 0%,#a89479 50%,#7e6b55 100%);opacity:.85;-webkit-mask-image:linear-gradient(90deg,#000 70%,transparent);mask-image:linear-gradient(90deg,#000 70%,transparent)}
.hero h1{left:672px;top:150px;font-size:42px;line-height:1.2;font-weight:600;color:var(--ink)}
.hero .lead{left:672px;top:266px;font-size:19px;color:var(--green);font-weight:500}
.hero .search{left:688px;top:376px;width:200px;height:42px;border-radius:21px 0 0 21px;background:var(--white);border:1px solid var(--line);font-size:13px;color:var(--muted);padding:12px 20px}
.hero .btn{left:892px;top:376px;width:126px;height:42px;border-radius:0 21px 21px 0}
.notch{top:540px;left:582px;width:36px;height:20px;background:var(--white);clip-path:polygon(50% 0,100% 100%,0 100%)}

/* services */
.services{top:640px;left:0;width:1200px;height:360px;background:var(--green-soft)}
.services h2{left:120px;top:88px;font-size:26px;font-weight:500}
.services h2 span{color:var(--green);font-weight:600}
.services .intro{left:120px;top:132px;width:300px;font-size:14px;line-height:1.6;color:var(--slate)}
.services .btn{left:120px;top:196px;width:146px;height:42px}
.service{width:176px;text-align:center;font-size:14px;line-height:1.5;color:var(--slate);padding-top:30px}
.service svg{display:block;margin:0 auto 18px}
.service.featured{background:var(--slate);color:var(--white);height:140px}
.service.featured::after{content:"";position:absolute;left:78px;bottom:-12px;border:10px solid transparent;border-top-color:var(--slate);border-bottom:0}

/* about */
.about h2{left:186px;top:1120px;font-size:26px;font-weight:400;line-height:1.45}
.about h2 b{font-weight:600}
.ticks{left:186px;top:1222px;list-style:none;font-size:14px;color:var(--slate)}
.ticks li{display:flex;align-items:center;gap:12px;height:38px}
.about .btn{left:186px;top:1352px;width:160px;height:48px}
.about-mark{left:688px;top:1080px;width:392px;height:328px;border:3px solid var(--green);display:flex;align-items:center;justify-content:center}

/* testimonials */
.reviews{top:1500px;left:0;width:1200px;height:580px;background:var(--grey-bg)}
.reviews .rule{left:120px;top:64px;width:62px;height:4px;background:var(--green)}
.reviews h2{left:120px;top:84px;font-size:26px;font-weight:400}
.reviews h2 b{font-weight:600}
.card{top:172px;width:306px;height:296px;background:var(--white);border:1px solid var(--line);padding:24px 26px}
.avatar{width:58px;height:58px;border-radius:50%;background:linear-gradient(135deg,#e9c9a5,#c79a6e);margin:0 auto 22px}
.card .who{display:flex;justify-content:space-between;font-size:13px;font-weight:600}
.stars{color:#f4b400;letter-spacing:2px}
.card p{font-size:12px;line-height:1.6;color:var(--muted);margin-top:10px}
.card .date{font-size:11px;color:#9aa0a6;margin-top:12px}
.card .tag{font-size:12px;color:var(--green);margin-top:4px;font-weight:500}
.dots{top:500px;left:570px;display:flex;gap:10px}
.dots i{width:10px;height:10px;border-radius:50%;background:#c6ccd2;display:block}
.dots i.on{background:var(--green)}

/* cta */
.cta{top:2080px;left:0;width:1200px;height:240px;background:var(--green);overflow:hidden}
.cta .ring{border:40px solid rgba(255,255,255,.08);border-radius:50%}
.cta h2{left:120px;top:72px;font-size:30px;font-weight:600;color:var(--white)}
.cta p{left:120px;top:124px;font-size:28px;font-weight:300;color:var(--white)}
.cta .btn{left:888px;top:100px;width:196px;height:50px;background:var(--white);color:var(--ink);border-radius:25px}

/* footer */
.footer{top:2320px;left:0;width:1200px;height:432px;background:var(--navy);color:#c7cbd6}
.footer .brand{left:120px;top:90px;color:var(--white)}
.footer .phone{left:120px;top:176px;font-size:22px;font-weight:500;color:var(--white)}
.footer .blurb{left:120px;top:216px;width:300px;font-size:13px;line-height:1.6}
.footer h4{font-size:15px;font-weight:600;color:var(--white)}
.quick{left:500px;top:90px}
.quick ul{list-style:none;margin-top:14px;font-size:13px;line-height:2}
.write{left:732px;top:90px}
.write p{font-size:12px;margin-top:12px}
.subscribe{display:flex;margin-top:18px}
.subscribe span{width:180px;height:40px;background:var(--white);border-radius:20px 0 0 20px;color:var(--muted);font-size:12px;padding:12px 18px}
.subscribe b{width:110px;height:40px;background:var(--green);border-radius:0 20px 20px 0;color:var(--white);font-size:13px;font-weight:500;display:flex;align-items:center;justify-content:center}
.follow{margin-top:24px}
.socials{display:flex;gap:12px;margin-top:12px}
.socials i{width:22px;height:22px;border-radius:50%;background:#3a425e;display:block}
.copy{left:0;top:370px;width:1200px;text-align:center;font-size:12px;border-top:1px solid #2c3450;padding-top:20px}
</style>
</head>
<body>

<header class="nav abs">
  <div class="brand abs"><span class="brand-dot"></span>FIXORA</div>
  <nav class="nav-links abs">
    <a class="active">Home</a><a>Services</a><a>Contact</a><a>Login</a>
  </nav>
  <a class="btn btn-green abs">Book A Services</a>
</header>

<section class="hero abs">
  <div class="hero-photo abs" role="img" aria-label="Smiling family of four standing in a bright living room"></div>
  <h1 class="abs">Home Maintenance<br>Made simple</h1>
  <p class="lead abs">One Call Can Solve All Your House Problems</p>
  <div class="search abs">What Do you Need</div>
  <a class="btn btn-dark abs">Get Help</a>
  <div class="notch abs"></div>
</section>

<section class="services abs">
  <h2 class="abs">Our <span>Services</span></h2>
  <p class="intro abs">Lorem ipsum is simply dummy text of the printing and typesetting industry.</p>
  <a class="btn btn-green abs">View Services</a>

  <div class="service abs" style="left:516px;top:92px">
    <svg width="44" height="44" viewBox="0 0 44 44" fill="none" stroke="#35b24a" stroke-width="2.5"><path d="M24 4 12 24h10l-4 16 14-22H22z"/></svg>
    Electrician<br>Services
  </div>
  <div class="service featured abs" style="left:712px;top:92px">
    <svg width="44" height="44" viewBox="0 0 44 44" fill="none" stroke="#ffffff" stroke-width="2.5"><rect x="8" y="6" width="28" height="32" rx="3"/><circle cx="22" cy="26" r="7"/><path d="M14 13h16"/></svg>
    DJ For Your<br>Party Services
  </div>
  <div class="service abs" style="left:908px;top:92px">
    <svg width="44" height="44" viewBox="0 0 44 44" fill="none" stroke="#35b24a" stroke-width="2.5"><circle cx="15" cy="28" r="9"/><circle cx="29" cy="28" r="9"/><path d="M15 19 22 8l7 11"/></svg>
    Mark Up Artist<br>For Wedding
  </div>
</section>

<section class="about">
  <h2 class="abs">A simple way To<br><b>Take Care of Everything</b></h2>
  <ul class="ticks abs">
    <li><svg width="18" height="18" viewBox="0 0 18 18" fill="none" stroke="#35b24a" stroke-width="2"><circle cx="9" cy="9" r="8"/><path d="m5 9 3 3 5-6"/></svg>Trusted technicians in your neighborhood</li>
    <li><svg width="18" height="18" viewBox="0 0 18 18" fill="none" stroke="#35b24a" stroke-width="2"><circle cx="9" cy="9" r="8"/><path d="m5 9 3 3 5-6"/></svg>Guaranteed parts and service + 24/7 support</li>
    <li><svg width="18" height="18" viewBox="0 0 18 18" fill="none" stroke="#35b24a" stroke-width="2"><circle cx="9" cy="9" r="8"/><path d="m5 9 3 3 5-6"/></svg>Hundreds of repair and install options</li>
  </ul>
  <a class="btn btn-dark abs">Learn More</a>
  <div class="about-mark abs"><div class="brand"><span class="brand-dot"></span>FIXORA</div></div>
</section>

<section class="reviews abs">
  <div class="rule abs"></div>
  <h2 class="abs">Don't just take <b>our word for it</b></h2>

  <article class="card abs" style="left:120px">
    <div class="avatar" role="img" aria-label="Client portrait"></div>
    <div class="who"><span>Client Name</span><span class="stars">★★★★★</span></div>
    <p>Lorem Ipsum is simply dummy text of the printing and typesetting industry. Lorem Ipsum has been the industry's.</p>
    <div class="date">October 3, 2020</div>
    <div class="tag">Electrician Services</div>
  </article>
  <article class="card abs" style="left:447px">
    <div class="avatar" role="img" aria-label="Client portrait"></div>
    <div class="who"><span>Client Name</span><span class="stars">★★★★★</span></div>
    <p>Lorem Ipsum is simply dummy text of the printing and typesetting industry. Lorem Ipsum has been the industry's.</p>
    <div class="date">October 3, 2020</div>
    <div class="tag">Electrician Services</div>
  </article>
  <article class="card abs" style="left:774px">
    <div class="avatar" role="img" aria-label="Client portrait"></div>
    <div class="who"><span>Client Name</span><span class="stars">★★★★★</span></div>
    <p>Lorem Ipsum is simply dummy text of the printing and typesetting industry. Lorem Ipsum has been the industry's.</p>
    <div class="date">October 3, 2020</div>
    <div class="tag">Electrician Services</div>
  </article>
  <div class="dots abs"><i></i><i class="on"></i><i></i></div>
</section>

<section class="cta abs">
  <div class="ring abs" style="left:-120px;top:-60px;width:320px;height:320px"></div>
  <div class="ring abs" style="left:1000px;top:80px;width:360px;height:360px"></div>
  <h2 class="abs">Ready to getstarted?</h2>
  <p class="abs">A simple way to take care of everything</p>
  <a class="btn abs">Book A Services</a>
</section>

<footer class="footer abs">
  <div class="brand abs"><span class="brand-dot"></span>FIXORA</div>
  <div class="phone abs">+1 (555) 010-2040</div>
  <p class="blurb abs">Be able to sign up with your name and keep every home job in one place.</p>
  <div class="quick abs">
    <h4>Quick Links</h4>
    <ul><li>Home</li><li>About Us</li><li>Services</li><li>Book A Services</li><li>Site Map</li><li>Contact Us</li></ul>
  </div>
  <div class="write abs">
    <h4>WRITE TO US</h4>
    <p>Provide your email below to subscribe to our newsletter</p>
    <div class="subscribe"><span>Email address</span><b>Subscribe</b></div>
    <h4 class="follow">FOLLOW US</h4>
    <div class="socials"><i></i><i></i><i></i><i></i><i></i></div>
  </div>
  <div class="copy abs">Copyright 2020 fixora.example</div>
</footer>

</body>
</html>
```